College Advising Business Card Design

We need a business card design for a new company. We advise students and their families on finding the right colleges to apply to; the application process; creating resumes; writing essays; and once students are accepted, figuring out what the best fit is. We pride ourselves on highly personal service, and we travel the country to learn about schools. The visual we have used on our website is a picture of a graduation caps tossed into the blue sky. See my website.

Target Market(s)

Parents of high school students

Industry/Entity Type

Travel

Contact Information for Business Card

COLLEGE IS THE DREAM. LET US HELP YOU FIND THE DESTINATION.

Marta Delvecchi Ornbrook and Associates
College Admissions Advising and Essay Guidance
enroll@martadelvecchiornbrook.example
555-418-PATH (7284)
Follow us on Friendlane

```html
<!DOCTYPE html>
<html lang="en">
<head>
<meta charset="utf-8">
<title>Marta Delvecchi Ornbrook and Associates – Business Card</title>
<link rel="stylesheet" href="https://fonts.googleapis.com/css2?family=Cormorant+Garamond:wght@400;500&family=Questrial&display=swap">
<style>
  :root {
    --page-bg: #eceef0;
    --card-blue: #3db8ec;
    --cloud-white: #ffffff;
    --panel-blue: #cdebf8;
    --headline-blue: #2aa9e3;
    --text-grey: #6f7478;
    --contact-grey: #7d8387;
  }
  * { margin: 0; padding: 0; box-sizing: border-box; }
  html, body {
    width: 1200px;
    height: 902px;
    overflow: hidden;
    background: var(--page-bg);
  }
  .canvas {
    position: relative;
    width: 1200px;
    height: 902px;
  }
  .business-card {
    position: absolute;
    left: 100px;
    top: 165px;
    width: 1000px;
    height: 571px;
    background: var(--card-blue);
    border-radius: 6px;
    overflow: hidden;
    box-shadow: 0 6px 18px rgba(0,0,0,0.18);
  }
  .sky-area {
    position: absolute;
    left: 40px;
    top: 34px;
    width: 920px;
    height: 503px;
    background: radial-gradient(ellipse at center, var(--cloud-white) 78%, #f2fafe 100%);
    border-radius: 80px;
  }
  .card-content {
    position: absolute;
    inset: 0;
    display: flex;
    flex-direction: column;
    align-items: center;
    text-align: center;
  }
  .headline {
    margin-top: 80px;
    font-family: "Cormorant Garamond", serif;
    font-weight: 500;
    font-size: 46px;
    letter-spacing: 2px;
    color: var(--headline-blue);
    text-transform: uppercase;
    line-height: 1;
  }
  .subline {
    margin-top: 8px;
    font-family: "Cormorant Garamond", serif;
    font-weight: 500;
    font-size: 29px;
    letter-spacing: 1.5px;
    color: var(--text-grey);
    text-transform: uppercase;
    line-height: 1;
  }
  .contact-panel {
    margin-top: 22px;
    width: 700px;
    padding: 26px 20px;
    background: var(--panel-blue);
    border-radius: 18px;
    font-family: "Questrial", sans-serif;
    font-size: 25px;
    line-height: 1.32;
    color: var(--contact-grey);
  }
  .follow-line {
    margin-top: 36px;
    font-family: "Cormorant Garamond", serif;
    font-weight: 500;
    font-size: 30px;
    letter-spacing: 1.5px;
    color: var(--text-grey);
    text-transform: uppercase;
  }
</style>
</head>
<body>
<main class="canvas">
  <section class="business-card">
    <div class="sky-area" role="img" aria-label="Large white cloud shape on a blue sky behind the card text"></div>
    <div class="card-content">
      <h1 class="headline">College is the dream.</h1>
      <p class="subline">Let us help you find the destination.</p>
      <div class="contact-panel">
        <p class="company-name">Marta Delvecchi Ornbrook and Associates</p>
        <p class="services">College Admissions Advising and Essay Guidance</p>
        <p class="email">enroll@martadelvecchiornbrook.example</p>
        <p class="phone">555-418-PATH (7284)</p>
      </div>
      <p class="follow-line">Follow us on Friendlane</p>
    </div>
  </section>
</main>
</body>
</html>
```